Commercial Waterproofing Modern Business Cards

We are a Commercial Waterproofing company. We do a variety of jobs on the exterior of buildings. We repel from the top or scaffold to reach the areas. Cut out and recaulk expansion joints and apply sealants, brick/concrete repairs, seal window frame perimeters, and much more. Our website is www.tallwallmend.net.
We are looking for a new business card design that would look more modern and cutting edge. We like the transparent paper and had thought about using our logo, but maybe pulling it apart to where the building part is kind of in the background. I have attached 2 different logos that we use regularly. We want the design to be a little funky, but professional at the same time. We really don't want the logo to be incorporated by itself, but you can use the logo and take out the buildings and just use the name or vice versa. Please don't just put the logo on the card and the words around that.

Target Market(s)

Property Managers/Building Maintenance

Industry/Entity Type

Business

Contact Information for Business Card

Daniel Ostrander President
Office (555)418-7290
Mobile (555)602-3947

Font styles to use
Serif

Requirements
Must have
• Nice overall design, somehow pulling from the logo for the design
Nice to have
• Look artsy and modern with a nice quality paper
Should not have
• Too many words or distracting designs. The logo 'as is'

```html
<!DOCTYPE html>
<html lang="en">
<head>
<meta charset="utf-8">
<title>Tall Wall Mend – Business Card</title>
<link href="https://fonts.googleapis.com/css2?family=Ubuntu:wght@400;500&display=swap" rel="stylesheet">
<style>
  :root {
    --backdrop: #2c3a52;
    --card-frost: #e4e8ec;
    --card-edge: #f3f5f7;
    --brand-blue: #2b5c9c;
    --panel-blue: #1d4f8c;
    --panel-line: #3a6aa4;
    --name-navy: #1f3f73;
    --sky-light: #e9f2fa;
    --sky-mid: #b9d3ea;
    --icon-cyan: #8fd0f0;
    --white: #ffffff;
  }
  * { box-sizing: border-box; margin: 0; padding: 0; }
  html, body {
    width: 1200px;
    height: 1000px;
    overflow: hidden;
    background: var(--backdrop);
    font-family: "Ubuntu", sans-serif;
  }
  .card {
    position: absolute;
    left: 179px;
    top: 251px;
    width: 842px;
    height: 498px;
    border-radius: 26px;
    background: linear-gradient(160deg, var(--card-edge) 0%, var(--card-frost) 60%, #d6dbe1 100%);
    box-shadow: 0 20px 50px rgba(0,0,0,0.35);
  }
  .brand {
    position: absolute;
    left: 40px;
    top: 100px;
    width: 340px;
    height: 320px;
    display: flex;
    align-items: center;
    justify-content: center;
  }
  .brand-name {
    font-weight: 500;
    font-size: 44px;
    color: var(--brand-blue);
    letter-spacing: 0.5px;
  }
  .name-panel {
    position: absolute;
    left: 410px;
    top: 113px;
    width: 400px;
    height: 77px;
    background: linear-gradient(120deg, var(--sky-mid) 0%, var(--sky-light) 45%, #f6f9fc 100%);
    text-align: right;
    padding: 10px 50px 0 0;
  }
  .person-name {
    font-size: 26px;
    color: var(--name-navy);
    letter-spacing: 0.5px;
    line-height: 32px;
  }
  .person-title {
    font-size: 21px;
    color: var(--name-navy);
    line-height: 28px;
  }
  .contact-panel {
    position: absolute;
    left: 410px;
    top: 198px;
    width: 400px;
    height: 216px;
    background: var(--panel-blue);
  }
  .contact-row {
    height: 72px;
    display: flex;
    align-items: center;
    justify-content: flex-end;
    padding-right: 16px;
    border-bottom: 1px solid var(--panel-line);
    color: var(--white);
    font-size: 26px;
    letter-spacing: 1.5px;
  }
  .contact-row:last-child { border-bottom: none; font-size: 24px; letter-spacing: 0.5px; }
  .contact-row svg { margin-left: 22px; flex: none; }
</style>
</head>
<body>
  <div class="card">
    <div class="brand">
      <span class="brand-name">Tall Wall Mend</span>
    </div>

    <div class="name-panel">
      <div class="person-name">Daniel Ostrander</div>
      <div class="person-title">President</div>
    </div>

    <div class="contact-panel">
      <div class="contact-row">
        <span class="contact-text">(555)418-7290</span>
        <svg class="icon-phone" width="20" height="22" viewBox="0 0 20 22" aria-hidden="true">
          <path d="M5 1 L8 6 L6 8 C7 12 9 15 12 16 L14 14 L18 17 L16 21 C8 20 2 12 2 3 Z" fill="var(--icon-cyan)"/>
        </svg>
      </div>
      <div class="contact-row">
        <span class="contact-text">(555)602-3947</span>
        <svg class="icon-mobile" width="20" height="26" viewBox="0 0 20 26" aria-hidden="true">
          <rect x="3" y="1" width="14" height="24" rx="2" fill="none" stroke="var(--icon-cyan)" stroke-width="2"/>
          <line x1="3" y1="20" x2="17" y2="20" stroke="var(--icon-cyan)" stroke-width="1.5"/>
        </svg>
      </div>
      <div class="contact-row">
        <span class="contact-text">www.tallwallmend.net</span>
        <svg class="icon-screen" width="22" height="20" viewBox="0 0 22 20" aria-hidden="true">
          <rect x="1" y="2" width="20" height="12" fill="var(--icon-cyan)"/>
          <rect x="8" y="14" width="6" height="3" fill="var(--icon-cyan)"/>
          <rect x="5" y="17" width="12" height="2" fill="var(--icon-cyan)"/>
        </svg>
      </div>
    </div>
  </div>
</body>
</html>
```